Davit Catalog

We need a catalog and possible up to 8 total to describe the equipment we provide. The davit system is one piece to suspending workers on the sides of buildings. The final design should show pictures and engineered details of the davit systems we supply along with photos for reference. Must be better than competitors!

Target Market(s)

architects, general contractors

Industry/Entity Type

Window Cleaning

Colors
0455a3
ec1f27
ffffff

```html
<!DOCTYPE html>
<html lang="en">
<head>
<meta charset="utf-8">
<title>Davit Catalog Covers</title>
<link rel="stylesheet" href="https://fonts.googleapis.com/css2?family=Open+Sans:ital,wght@0,400;0,700;1,700&display=swap">
<style>
  :root {
    --brand-blue: #0455a3;
    --brand-red: #ec1f27;
    --white: #ffffff;
    --paper-top: #f5f5f5;
    --paper-bottom: #e2e2e2;
    --stage: #efece7;
  }
  * { margin: 0; padding: 0; box-sizing: border-box; }
  html, body {
    width: 1200px;
    height: 880px;
    overflow: hidden;
    background: var(--stage);
    font-family: "Open Sans", Arial, sans-serif;
  }
  .spread { position: relative; width: 1200px; height: 880px; }
  .cover {
    position: absolute;
    top: 247px;
    width: 560px;
    height: 386px;
    overflow: hidden;
    box-shadow: 0 4px 10px rgba(0, 0, 0, 0.18);
  }
  .cover--front {
    left: 25px;
    background: linear-gradient(180deg, var(--paper-top), var(--paper-bottom));
  }
  .cover--back { left: 615px; background: var(--brand-blue); }
  .photo { position: absolute; }

  .photo--towers {
    left: 0; top: 23px; width: 274px; height: 219px;
    background:
      linear-gradient(180deg, rgba(0,0,0,0) 62%, rgba(60,40,30,0.55) 100%),
      linear-gradient(90deg, #d9dcd8 0%, #c8ccc6 20%, #2d5aa8 34%, #3466b4 58%, #dfe7ea 74%, #b9c6c9 100%);
  }
  .photo--facade {
    left: 289px; top: 23px; width: 115px; height: 103px;
    background: linear-gradient(120deg, #2f63b3 0%, #5b87c4 35%, #9a9896 55%, #7b7772 80%, #4e4b48 100%);
  }
  .photo--rooftop-davits {
    left: 418px; top: 23px; width: 116px; height: 103px;
    background: linear-gradient(180deg, #7f97b8 0%, #b9c3cf 45%, #8f8a82 62%, #d6d6d4 78%, #e4e4e2 100%);
  }
  .photo--anchor-install {
    left: 289px; top: 140px; width: 115px; height: 102px;
    background: linear-gradient(135deg, #5a4634 0%, #8a6f55 40%, #b8b3ad 62%, #7a6552 100%);
  }
  .photo--parapet {
    left: 418px; top: 140px; width: 116px; height: 102px;
    background: linear-gradient(180deg, #3f76c4 0%, #7fa2cf 30%, #7c8a72 48%, #3e3e40 70%, #2a2a2c 100%);
  }

  .tagline {
    position: absolute;
    left: 49px;
    top: 260px;
    color: var(--brand-blue);
    font-size: 19px;
    line-height: 26px;
    font-weight: 700;
    font-style: italic;
  }
  .brand {
    position: absolute;
    right: 25px;
    top: 266px;
    display: flex;
    align-items: center;
    gap: 8px;
  }
  .brand__mark { width: 26px; height: 26px; background: var(--brand-red); }
  .brand__name {
    color: var(--brand-red);
    font-size: 30px;
    font-weight: 700;
    line-height: 1;
    letter-spacing: 0.5px;
  }
  .band-red {
    position: absolute;
    left: 0; bottom: 0;
    width: 100%;
    height: 22px;
    background: var(--brand-red);
  }

  .photo--tower-upview {
    left: 0; top: 23px; width: 560px; height: 341px;
    background:
      linear-gradient(160deg, rgba(255,255,255,0) 40%, rgba(40,50,60,0.35) 100%),
      linear-gradient(115deg, #6f95cf 0%, #c7d3e2 18%, #8c96a2 32%, #e6eaee 46%, #9aa5b2 58%, #d3dbe4 70%, #7d8fa6 84%, #a9bfdc 100%);
  }
  .band-blue-top {
    position: absolute;
    left: 0; top: 0;
    width: 100%;
    height: 23px;
    background: var(--brand-blue);
  }
  .band-blue-overlay {
    position: absolute;
    left: 0; top: 242px;
    width: 100%;
    height: 122px;
    background: rgba(4, 85, 163, 0.84);
  }
  .contact {
    position: absolute;
    right: 47px;
    top: 262px;
    text-align: right;
    color: var(--white);
    font-size: 8.5px;
    line-height: 10.5px;
    font-style: normal;
  }
  .contact__web { margin-top: 10px; }
</style>
</head>
<body>
  <main class="spread">
    <section class="cover cover--front">
      <div class="photo photo--towers" role="img" aria-label="Residential high-rise towers under a blue sky"></div>
      <div class="photo photo--facade" role="img" aria-label="Glass and stone building facade seen from below"></div>
      <div class="photo photo--rooftop-davits" role="img" aria-label="Rooftop davit arms with workers at the roof edge"></div>
      <div class="photo photo--anchor-install" role="img" aria-label="Worker installing a roof anchor post"></div>
      <div class="photo photo--parapet" role="img" aria-label="Davit system along a rooftop parapet"></div>
      <h1 class="tagline">Engineered<br>Fall Protection Solutions</h1>
      <div class="brand">
        <span class="brand__mark"></span>
        <span class="brand__name">CORVEX</span>
      </div>
      <div class="band-red"></div>
    </section>

    <section class="cover cover--back">
      <div class="photo photo--tower-upview" role="img" aria-label="Glass tower viewed upward from street level"></div>
      <div class="band-blue-top"></div>
      <div class="band-blue-overlay"></div>
      <address class="contact">
        <p>2240 Harbour Lane</p>
        <p>Northport, BC V0X 1A0 Canada</p>
        <p>Tel: 555 210 0148 &nbsp;|&nbsp; Fax: 555 210 0149</p>
        <p>Email: sales@corvex-anchor.example</p>
        <p class="contact__web">www.corvex-anchor.example</p>
      </address>
      <div class="band-red"></div>
    </section>
  </main>
</body>
</html>
```